Website design for a private chef business

Need a website that is eye catching and with easy contact, newsletter signups and scheduling tool/calendar . Website is chefdw.com and geographic focus is The Woodlands, TX and Austin, TX. I cook all styles of cuisine so anything is possible and I'm a veteran of Afghanistan via the Vale Guard so if you could mention it's a veteran owned business

Target Market(s)

Affluent families and successful professionals in TheWoodlands, TX and Austin, TX

Industry/Entity Type

Business

Number of Pages Required

1 page

Requirements
Must have
• Eyecatching visuals
• Contact form
• Newsletter sign up
• Scheduling tool
Should not have
• N/a

```html
<!DOCTYPE html>
<html lang="en">
<head>
<meta charset="utf-8">
<title>Chef Dane — Private Chef</title>
<link rel="stylesheet" href="https://fonts.googleapis.com/css2?family=Montserrat:wght@600;700&family=Raleway:wght@300;400;500;600&display=swap">
<style>
:root{
  --red:#d0321f;
  --red-deep:#b52617;
  --ink:#333333;
  --grey-text:#8a8a8a;
  --page:#f2f2f2;
  --white:#ffffff;
  --dark:#2b2b2b;
  --calendar:#3d3d3d;
  --field-line:#cfcfcf;
}
*{box-sizing:border-box;margin:0;padding:0}
html,body{width:1200px;height:4651px;overflow:hidden}
body{position:relative;background:var(--page);font-family:'Raleway',sans-serif;color:var(--ink)}
.abs{position:absolute}

/* header */
.site-header{left:0;top:0;width:1200px;height:190px;background:var(--white)}
.logo{left:0;top:0;width:145px;height:190px;background:var(--red);color:var(--white);font:600 34px/1.05 'Raleway',sans-serif;padding:48px 0 0 20px}
.main-nav{left:340px;top:88px;display:flex;gap:0}
.main-nav a{font-size:15px;color:var(--ink);text-decoration:none;margin-right:28px;position:relative}
.main-nav a.active{color:var(--red)}
.main-nav a.active::after{content:"";position:absolute;left:-8px;right:-8px;top:38px;height:3px;background:var(--red)}

/* hero */
.hero{left:0;top:190px;width:1200px;height:525px;background:linear-gradient(90deg,#3a3a3a,#1e1e1e 50%,#333)}
.hero-title{left:0;width:1200px;top:380px;text-align:center;font:700 72px/1 'Montserrat',sans-serif;color:var(--white);letter-spacing:1px}
.hero-title span{color:var(--red)}
.hero-sub{left:0;width:1200px;top:475px;text-align:center;font:400 36px/1 'Raleway',sans-serif;color:#e6e6e6}

/* about */
.about-photo{left:660px;top:730px;width:400px;height:640px;background:radial-gradient(ellipse at 50% 40%,#f7f7f7,#dedede)}
.about-text{left:148px;top:770px;width:380px;color:var(--white)}
.about-text h2{font:400 60px/1 'Raleway',sans-serif;margin-bottom:40px}
.about-text p{font-size:16px;line-height:1.4;margin-bottom:40px}
.btn{display:inline-block;font-size:17px;text-align:center;border-radius:20px;line-height:40px;height:40px}
.btn-white{background:var(--white);color:var(--red)}
.btn-red{background:var(--red);color:var(--white)}

/* section heads */
.section-title{left:0;width:1200px;text-align:center;font:400 44px/1 'Raleway',sans-serif}
.rule{left:520px;width:160px;height:3px;background:var(--red)}
.rule.light{background:var(--white)}

/* gallery */
.tile{width:600px;height:336px}
.tile-feature{background:var(--red);color:var(--white);text-align:center}
.tile-feature p{font-size:17px;line-height:1.3;margin-top:18px}

/* newsletter */
.newsletter{left:0;top:2542px;width:1200px;height:450px;background:var(--red)}
.email-field{left:418px;top:2700px;width:410px;height:71px;background:#b04a3f;color:#e5c6c1;font:italic 20px/71px 'Raleway',sans-serif;padding-left:34px}
.subscribe{left:527px;top:2855px;width:180px;height:59px;border-radius:14px;background:var(--white);color:var(--red);font:italic 22px/59px 'Raleway',sans-serif;text-align:center}

/* schedule */
.schedule-note{left:148px;width:390px;font-size:16px;line-height:1.35;color:var(--grey-text)}
.calendar{left:670px;top:3147px;width:378px;height:363px;background:var(--calendar);color:var(--white);padding:16px 18px}
.calendar h3{text-align:center;font:600 26px/1 'Raleway',sans-serif;margin-bottom:14px}
.calendar table{width:100%;border-collapse:collapse;text-align:center}
.calendar th{font-size:14px;font-weight:600;height:30px;border-bottom:1px solid #5a5a5a}
.calendar td{font-size:22px;height:46px}

/* honor */
.honor{left:0;top:3612px;width:1200px;height:480px;background:linear-gradient(100deg,#b83a30,#c9463a 45%,#a3261c)}
.honor-sub{left:0;width:1200px;top:3752px;text-align:center;color:var(--white);font-size:26px}
.honor-col{width:440px;color:var(--white);font-size:17px;line-height:1.32}

/* contact */
.field{border:2px solid var(--field-line);color:#aaa;font-size:16px;padding:10px 14px}
.socials{left:853px;top:4523px;display:flex;gap:6px}
.socials span{width:46px;height:50px;background:#6e6e6e;border-radius:4px}
</style>
</head>
<body>

<header class="abs site-header">
  <div class="abs logo">LOGO<br>HERE</div>
  <nav class="abs main-nav">
    <a class="active">Home</a><a>About Me</a><a>Recipes</a><a>Books</a><a>Gallery</a><a>News</a><a>Press kit</a><a>Partners</a><a>Contact</a>
  </nav>
</header>

<section class="abs hero" role="img" aria-label="Chef team at work in a kitchen, dark toned"></section>
<h1 class="abs hero-title">CHEF <span>DANE</span></h1>
<p class="abs hero-sub">To Make Your Life Delicious</p>

<svg class="abs" style="left:0;top:715px" width="1200" height="655" aria-hidden="true">
  <rect width="1200" height="655" fill="#f2f2f2"/>
  <polygon points="0,0 707,0 465,655 0,655" fill="#d0321f"/>
</svg>
<div class="abs about-photo" role="img" aria-label="Portrait of the chef in white jacket and toque, arms crossed"></div>
<div class="abs about-text">
  <h2>who i am</h2>
  <p>Lorem Ipsum is simply dummy text of the printing and typesetting industry. Lorem Ipsum has been the industry's standard dummy text ever since the 1500s,</p>
  <p>Lorem Ipsum is simply dummy text of the printing and typesetting industry. Lorem Ipsum has been the industry's standard dummy text ever since the 1500s,</p>
  <p>Lorem Ipsum is simply dummy text of the printing and typesetting industry. Lorem Ipsum has been the industry's standard dummy text ever since the 1500s,</p>
  <span class="btn btn-white" style="width:130px">More</span>
</div>

<h2 class="abs section-title" style="top:1412px">food gallery</h2>
<div class="abs rule" style="top:1486px"></div>

<div class="abs tile tile-feature" style="left:0;top:1535px">
  <svg width="160" height="120" viewBox="0 0 160 120" style="margin-top:70px" aria-hidden="true">
    <circle cx="80" cy="18" r="8" fill="none" stroke="#fff" stroke-width="6"/>
    <path d="M28 92 A52 52 0 0 1 132 92" fill="none" stroke="#fff" stroke-width="6"/>
    <line x1="10" y1="104" x2="150" y2="104" stroke="#fff" stroke-width="6" stroke-linecap="round"/>
  </svg>
  <p>Lorem Ipsum is simply dummy<br>text of the printing</p>
</div>
<div class="abs tile" style="left:600px;top:1535px;background:linear-gradient(135deg,#e8d2a8,#c9a85c 50%,#7fa54a)" role="img" aria-label="Stacked club sandwich"></div>
<div class="abs tile" style="left:0;top:1871px;background:linear-gradient(120deg,#6b3a2a,#a04a2e 50%,#d44a2c)" role="img" aria-label="Seared duck breast with cherry tomatoes"></div>
<div class="abs tile" style="left:600px;top:1871px;background:radial-gradient(circle at 50% 55%,#9a3218,#c86a3e 55%,#efe9e2)" role="img" aria-label="Bowl of stew with herbs"></div>
<div class="abs tile" style="left:0;top:2207px;background:linear-gradient(120deg,#f6e7c8,#f2a417 40%,#c45a2a)" role="img" aria-label="Fried egg with bacon"></div>
<div class="abs tile" style="left:600px;top:2207px;background:radial-gradient(circle at 60% 60%,#e8c27a,#f1e5cf 60%,#f4f1ec)" role="img" aria-label="Pasta with tomatoes on a white plate"></div>

<section class="abs newsletter"></section>
<h2 class="abs section-title" style="top:2580px;color:var(--white)">news letters</h2>
<div class="abs rule light" style="top:2645px;background:#8a1e12"></div>
<div class="abs email-field">enter your email</div>
<div class="abs subscribe">subscribe</div>

<h2 class="abs section-title" style="top:3030px;color:#555">schedule</h2>
<div class="abs rule" style="top:3094px"></div>
<p class="abs schedule-note" style="top:3164px">Lorem Ipsum is simply dummy text of the printing and typesetting industry. Lorem Ipsum has been the industry's</p>
<p class="abs schedule-note" style="top:3301px">Lorem Ipsum is simply dummy text of the printing and typesetting industry. Lorem Ipsum has been the industry's</p>
<p class="abs schedule-note" style="top:3437px">Lorem Ipsum is simply dummy text of the printing and typesetting industry. Lorem Ipsum has been the industry's</p>
<span class="abs btn btn-red" style="left:146px;top:3534px;width:126px;height:44px;line-height:44px">More</span>

<div class="abs calendar">
  <h3>November 2015</h3>
  <table>
    <tr><th>Mo</th><th>Tu</th><th>We</th><th>Th</th><th>Fr</th><th>Sa</th><th>Su</th></tr>
    <tr><td></td><td></td><td></td><td></td><td></td><td></td><td>1</td></tr>
    <tr><td>2</td><td>3</td><td>4</td><td>5</td><td>6</td><td>7</td><td>8</td></tr>
    <tr><td>9</td><td>10</td><td>11</td><td>12</td><td>13</td><td>14</td><td>15</td></tr>
    <tr><td>16</td><td>17</td><td>18</td><td>19</td><td>20</td><td>21</td><td>22</td></tr>
    <tr><td>23</td><td>24</td><td>25</td><td>26</td><td>27</td><td>28</td><td>29</td></tr>
    <tr><td>30</td><td></td><td></td><td></td><td></td><td></td><td></td></tr>
  </table>
</div>

<section class="abs honor" role="img" aria-label="Hands holding a cup before a flag, red toned"></section>
<h2 class="abs section-title" style="top:3648px;color:var(--white)">honor &amp; pride</h2>
<div class="abs rule light" style="top:3710px"></div>
<p class="abs honor-sub">I'm a veteran of afghanistan via the vale guard</p>
<p class="abs honor-col" style="left:148px;top:3812px">Lorem Ipsum is simply dummy text of the printing and typesetting industry. Lorem Ipsum has been the industry's<br>Lorem Ipsum is simply dummy text of the printing and typesetting industry. Lorem Ipsum has been the industry's</p>
<p class="abs honor-col" style="left:605px;top:3812px">Lorem Ipsum is simply dummy text of the printing and typesetting industry. Lorem Ipsum has been the industry's<br>Lorem Ipsum is simply dummy text of the printing and typesetting industry. Lorem Ipsum has been the industry's</p>
<span class="abs btn btn-white" style="left:146px;top:4021px;width:126px;height:38px;line-height:38px">More</span>

<h2 class="abs section-title" style="top:4124px">contact me</h2>
<div class="abs rule" style="top:4190px;left:540px;width:120px"></div>
<div class="abs field" style="left:161px;top:4262px;width:422px;height:56px">first name</div>
<div class="abs field" style="left:161px;top:4346px;width:422px;height:56px">lastname</div>
<div class="abs field" style="left:161px;top:4424px;width:422px;height:56px">email</div>
<div class="abs field" style="left:620px;top:4262px;width:422px;height:211px">your message</div>
<span class="abs btn btn-red" style="left:146px;top:4526px;width:124px;height:37px;line-height:37px">send</span>
<div class="abs socials" aria-label="Social links"><span></span><span></span><span></span><span></span></div>

</body>
</html>
```